Mandala Postcard Design

I am in need of a postcard to hand out at a Psychic Fair. I envision the card to having half-of-a Mandala (from my Sketchnook folder), touched up a bit to make it vibrant and bold. Others vendors will have cards w/photographic backgrounds doing yoga. I'd like mine to stand out for it's line-drawn "cartoonish" nature, solid-color nature. The wording would be my basic contact info and a short description ... something like: "Experience the Magic of Mandala Making ... Next Class will be held: (open space for writing, no lines) The art is contained in this Sketchnook folder. Lots to choose from, with my favorites being the stronger outlined designs.

https://www.sketchnook.example/Brightloom/media_set?set=a.20262926615637197.2184852941.783542196&type=3
Updates

I just uploaded a few new drawings that might work better, since they are more round. I want to minimize the white space, for instance, avoid having the left & right corners empty. Another idea could be to use 1/4 mandalas in the corners. I'm ready to make a decision. I want it to look great, but as I gain drawing experience, I'll need to update my cards. Thanks! I'm not sure if this the place for this comment, but I'll also be needing a DVD label for my tutorials, and a front page design for a mandala coloring book.

Target Market(s)

Primarily women interested in metaphysical, psychic, meditation, reiki and a basic interest in art.

Font styles to use
Serif
Sans Serif

Requirements
Should not have
• Should not be on a dark card, really should be a plain white background, it seems, in order to stand out.

```html
<!DOCTYPE html>
<html lang="en">
<head>
<meta charset="utf-8">
<title>Mandala Postcard – Front and Back</title>
<link href="https://fonts.googleapis.com/css2?family=Sniglet:wght@400;800&family=Delius&family=Poiret+One&display=swap" rel="stylesheet">
<style>
  :root {
    --stage: #000000;
    --card: #ffffff;
    --ink: #1a1a1a;
    --faint: #d9d9d9;
    --warm-red: #e8453c;
    --warm-orange: #f39a1e;
    --warm-yellow: #f6d21c;
    --lilac: #b9a7bd;
    --sky: #4f8fd6;
    --leaf: #3aa856;
  }
  * { box-sizing: border-box; margin: 0; padding: 0; }
  html, body { width: 1200px; height: 709px; overflow: hidden; background: var(--stage); }
  .stage { position: relative; width: 1200px; height: 709px; }

  .postcard { position: absolute; top: 14px; width: 523px; height: 678px; background: var(--card); overflow: hidden; color: var(--ink); }
  .postcard--front { left: 56px; }
  .postcard--back { left: 618px; }

  .abs { position: absolute; }

  /* front */
  .mandala-art { left: 0; top: 0; width: 523px; height: 330px; }
  .headline { font-family: "Sniglet", system-ui, sans-serif; font-weight: 800; font-size: 32px; letter-spacing: 1px; line-height: 1; }
  .headline--left { left: 42px; top: 334px; }
  .headline--right { left: 298px; top: 334px; }
  .subline { font-family: "Delius", cursive; font-size: 16px; letter-spacing: .5px; line-height: 1; }
  .subline--left { left: 42px; top: 374px; }
  .subline--right { left: 325px; top: 374px; }
  .squiggle { left: 0; }
  .front-squiggle { top: 388px; width: 480px; height: 30px; }
  .class-box { left: 8px; top: 416px; width: 500px; height: 252px; }
  .class-label { left: 0; width: 523px; top: 424px; text-align: center; font-family: "Delius", cursive; font-size: 15px; }
  .class-label span { background: var(--card); padding: 0 8px; }
  .front-url { left: 0; width: 523px; top: 648px; text-align: center; font-family: "Delius", cursive; font-size: 14px; }
  .front-url span { background: var(--card); padding: 0 8px; }

  /* back */
  .faint-mandala { left: 0; top: 0; width: 320px; height: 300px; }
  .faint-ornament { left: 400px; top: 330px; width: 123px; height: 230px; }
  .stamp-box { left: 404px; top: 48px; width: 71px; height: 96px; border: 1.5px solid var(--ink); border-radius: 9px; }
  .address-line { left: 336px; width: 140px; height: 0; border-top: 1.2px solid var(--ink); }
  .address-line--1 { top: 214px; }
  .address-line--2 { top: 252px; }
  .address-line--3 { top: 290px; }
  .back-title { left: 30px; top: 345px; font-family: "Sniglet", system-ui, sans-serif; font-weight: 800; font-size: 28px; letter-spacing: .5px; line-height: 1; }
  .back-subline { left: 28px; top: 382px; font-family: "Poiret One", system-ui, sans-serif; font-size: 27px; font-weight: 400; letter-spacing: 1px; line-height: 1; -webkit-text-stroke: .4px var(--ink); }
  .back-name { left: 28px; top: 418px; font-family: "Poiret One", system-ui, sans-serif; font-size: 37px; letter-spacing: 1.5px; line-height: 1; -webkit-text-stroke: .5px var(--ink); }
  .back-squiggle { top: 455px; width: 380px; height: 30px; }
  .follow-line { left: 30px; width: 460px; top: 594px; text-align: center; font-family: "Delius", cursive; font-size: 18px; letter-spacing: 1px; }
  .back-url { left: 30px; width: 460px; top: 624px; text-align: center; font-family: "Delius", cursive; font-size: 14px; }
</style>
</head>
<body>
<main class="stage">

  <section class="postcard postcard--front" aria-label="Postcard front">
    <svg class="abs mandala-art" viewBox="0 0 523 330" role="img" aria-label="Half of a vibrant hand-drawn mandala in red, orange, yellow, lilac, blue and green with bold black outlines">
      <defs>
        <radialGradient id="mandalaTones" cx="50%" cy="0%" r="100%">
          <stop offset="0%" stop-color="#f6d21c"/>
          <stop offset="35%" stop-color="#f39a1e"/>
          <stop offset="65%" stop-color="#e8453c"/>
          <stop offset="85%" stop-color="#b9a7bd"/>
          <stop offset="100%" stop-color="#4f8fd6"/>
        </radialGradient>
      </defs>
      <path d="M0 0 H523 V70 C505 170 440 250 370 280 L270 330 L170 285 C90 250 25 175 0 80 Z" fill="url(#mandalaTones)"/>
    </svg>

    <div class="abs headline headline--left">EXPERIENCE</div>
    <div class="abs headline headline--right">THE MAGIC</div>
    <div class="abs subline subline--left">OF MANDALA MAKING WITH</div>
    <div class="abs subline subline--right">NORA WHITFIELD</div>

    <svg class="abs squiggle front-squiggle" viewBox="0 0 480 30" aria-hidden="true">
      <path d="M0 18 C80 16 160 20 240 17 C270 16 292 15 298 10 C304 4 296 0 292 6 C288 14 300 20 330 19 C380 17 430 20 470 17" fill="none" stroke="var(--ink)" stroke-width="2" stroke-linecap="round"/>
      <circle cx="476" cy="20" r="1.6" fill="var(--ink)"/>
    </svg>

    <svg class="abs class-box" viewBox="0 0 500 252" aria-hidden="true">
      <path d="M6 10 L455 8 M455 8 C462 20 475 28 492 30 L490 245 L4 248 L6 10" fill="none" stroke="var(--ink)" stroke-width="1.6" stroke-linejoin="round"/>
      <path d="M455 8 C470 4 488 10 492 30 C480 26 466 24 458 30 C456 22 456 14 455 8 Z" fill="none" stroke="var(--ink)" stroke-width="1.6" stroke-linejoin="round"/>
    </svg>
    <div class="abs class-label"><span>Next Class will be held:</span></div>
    <div class="abs front-url"><span>www.sketchnook.example/MandalaCircle</span></div>
  </section>

  <section class="postcard postcard--back" aria-label="Postcard back">
    <svg class="abs faint-mandala" viewBox="0 0 320 300" role="img" aria-label="Faint grey line-drawn quarter mandala decoration">
      <path d="M0 0 H300 C320 90 290 200 200 260 C140 300 60 300 0 280 Z" fill="var(--faint)" opacity=".55"/>
    </svg>
    <svg class="abs faint-ornament" viewBox="0 0 123 230" role="img" aria-label="Faint grey line-drawn partial mandala ornament at the edge">
      <path d="M123 0 C60 40 30 80 30 115 C30 150 60 190 123 230 Z" fill="var(--faint)" opacity=".55"/>
    </svg>

    <div class="abs stamp-box" aria-label="Stamp space"></div>
    <div class="abs address-line address-line--1"></div>
    <div class="abs address-line address-line--2"></div>
    <div class="abs address-line address-line--3"></div>

    <div class="abs back-title">EXPERIENCE THE MAGIC</div>
    <div class="abs back-subline">OF MANDALA MAKING WITH</div>
    <div class="abs back-name">NORA WHITFIELD</div>

    <svg class="abs squiggle back-squiggle" viewBox="0 0 380 30" aria-hidden="true">
      <path d="M0 14 C60 12 120 16 180 14 C210 13 230 14 236 9 C242 3 234 -1 230 5 C226 13 238 19 268 18 C310 17 340 20 366 19" fill="none" stroke="var(--ink)" stroke-width="2" stroke-linecap="round"/>
      <circle cx="372" cy="21" r="1.6" fill="var(--ink)"/>
    </svg>

    <div class="abs follow-line">FOLLOW ME ON SKETCHNOOK AT</div>
    <div class="abs back-url">www.sketchnook.example/MandalaCircle</div>
  </section>

</main>
</body>
</html>
```